(Wix) Website Design Tweaks

The site: www.MarbleFinchCo.com
(The coding must be done within Wix. I will create a duplicate website so you can gain access and begin editing.)

My website contains my preferred text and images - but it needs to look more professional. My business focuses on "Corporate Messaging" and "Marketing Communications", so the website needs to look professional, but not too corporate. My clients range from very big companies to technology startups - the look and feel should be uncluttered, professional, and modern.

I want someone to review the pages, and make changes / suggestions focused on:
1) Fonts
2) Colors
3) Layout

If you have ideas for adding additional graphics, that's fine, but they should be consistent with what I already have . . . unless you think some / all of my images need to be changed.

My site is very, very small, and only contains 5 (very short) pages. There are no sub-pages. (One page is the contact page, with almost nothing except form fields.)

If you do a good job with my site, I may be able to provide you with additional work - many of my clients need website design tweaks, after I provide the verbiage.

```html
<!DOCTYPE html>
<html lang="en">
<head>
<meta charset="utf-8">
<title>Marble Finch — Inform. Influence. Sell.</title>
<link href="https://fonts.googleapis.com/css2?family=Montserrat:ital,wght@0,400;0,500;0,600;0,700;0,800;1,600;1,700&display=swap" rel="stylesheet">
<style>
:root{
  --brand:#00aeef;
  --ink:#1e1e1e;
  --muted:#7a7a7a;
  --paper:#ffffff;
  --mist:#f4f4f5;
  --field:#f6f6f7;
  --footer:#3b3b3d;
}
*{box-sizing:border-box;margin:0;padding:0}
html,body{width:1200px;height:3851px;overflow:hidden}
body{position:relative;font-family:'Montserrat',sans-serif;color:var(--ink);background:var(--paper)}
.abs{position:absolute}
.topline{left:0;top:0;width:1200px;height:4px;background:var(--brand);z-index:5}

/* header */
.logo{background:var(--brand);color:#fff;font-size:14px;line-height:15px;font-weight:500;display:flex;align-items:flex-end;padding:0 0 12px 14px}
.header-logo{left:147px;top:0;width:95px;height:90px;z-index:6}
.nav{top:40px;display:flex;z-index:6}
.nav a{position:absolute;white-space:nowrap;font-size:13px;font-weight:700;color:#fff;text-decoration:none;letter-spacing:.2px}
.nav a.active{color:var(--brand)}
.search{left:1007px;top:27px;width:42px;height:40px;background:var(--brand);z-index:6;display:flex;align-items:center;justify-content:center}

/* hero */
.hero-photo{left:0;top:0;width:1200px;height:699px;background:radial-gradient(ellipse at 62% 40%,#6f8fb3 0%,#2c3d58 35%,#121a29 70%,#0a0e17 100%)}
.hero-title{left:163px;top:272px;font-size:54px;line-height:65px;font-weight:800;color:#fff;letter-spacing:1px}

/* shared */
.section-title{font-style:italic;font-weight:600;font-size:44px;letter-spacing:.5px}
.copy{font-size:15px;line-height:21.5px}

.maze-photo{left:744px;top:645px;width:456px;height:434px;background:linear-gradient(160deg,#eceef1 0%,#d5d9df 45%,#b8bdc5 100%)}
.challenge-title{left:146px;top:770px}
.challenge-copy{left:149px;top:845px;width:545px;color:var(--muted)}

.help-band{left:0;top:1079px;width:1200px;height:394px;background:var(--brand)}
.meeting-photo{left:0;top:1079px;width:423px;height:394px;background:linear-gradient(120deg,#5b4a3b 0%,#8a7560 40%,#c8bcab 70%,#6e5e4d 100%)}
.help-title{left:511px;top:1190px;width:535px;text-align:right;color:#fff}
.help-copy{left:505px;top:1267px;width:541px;text-align:right;color:#fff}

/* expertise */
.expertise{left:0;top:1473px;width:1200px;height:734px;background:var(--mist)}
.expertise-title{left:0;top:1556px;width:1200px;text-align:center}
.card{width:191px;height:210px;background:#fff;display:flex;flex-direction:column;align-items:center;text-align:center;font-size:15px;line-height:18px;color:#444}
.card svg{margin-top:34px;width:76px;height:76px;fill:none;stroke:var(--brand);stroke-width:2.2;stroke-linecap:round;stroke-linejoin:round}
.card .label{flex:1;display:flex;align-items:center;padding:0 10px 6px}

/* clients */
.clients-title{left:0;top:2264px;width:1200px;text-align:center}
.client{width:164px;height:93px;background:#fff;box-shadow:0 2px 8px rgba(0,0,0,.12);display:flex;align-items:center;justify-content:center;text-align:center;font-size:17px;font-weight:600;color:#6b6b6b;line-height:20px}
.dot{top:2613px;width:13px;height:13px;background:#d0d0d2}

/* results */
.results-band{left:0;top:2709px;width:593px;height:388px;background:var(--brand)}
.results-photo{left:593px;top:2709px;width:607px;height:388px;background:radial-gradient(circle at 43% 62%,#fff4c4 0%,#f2b84b 9%,#8aa6bf 28%,#4c6f8d 55%,#2c3f50 100%)}
.results-title{left:148px;top:2796px;color:#fff}
.results-copy{left:148px;top:2870px;width:380px;color:#fff}

/* contact */
.connect-title{left:0;top:3171px;width:1200px;text-align:center}
.field{background:var(--field);height:44px;font-size:14px;color:#333;padding:15px 0 0 16px}
.submit{left:783px;top:3541px;width:96px;height:58px;background:var(--brand);color:#fff;font-size:13px;font-weight:700;display:flex;align-items:center;justify-content:center;letter-spacing:.5px}

/* footer */
.footer{left:0;top:3680px;width:1200px;height:171px;background:var(--footer)}
.footer-logo{left:147px;top:3680px;width:76px;height:75px;font-size:13px;padding:0 0 8px 6px}
.footer-rule{left:223px;top:3755px;width:830px;height:1px;background:#6a6a6c}
.footer-nav a{top:3717px;color:#fff}
.copyright{left:0;top:3806px;width:1200px;text-align:center;font-size:11px;color:#fff}
</style>
</head>
<body>

<div class="abs topline"></div>

<!-- header -->
<div class="abs logo header-logo">MARBLE &amp;<br>FINCH</div>
<nav class="abs nav">
  <a class="active" style="left:499px;top:0" href="#">HOME</a>
  <a style="left:575px;top:0" href="#">FINCHCAMP</a>
  <a style="left:692px;top:0" href="#">TESTIMONIALS</a>
  <a style="left:829px;top:0" href="#">TEAM</a>
  <a style="left:901px;top:0" href="#">CONTACT</a>
</nav>
<div class="abs search">
  <svg width="16" height="16" viewBox="0 0 16 16"><circle cx="6.5" cy="6.5" r="4.5" fill="none" stroke="#fff" stroke-width="2.2"/><line x1="10" y1="10" x2="14" y2="14" stroke="#fff" stroke-width="2.4" stroke-linecap="round"/></svg>
</div>

<!-- hero -->
<div class="abs hero-photo" role="img" aria-label="Speaker in a light blue shirt addressing a large conference audience"></div>
<h1 class="abs hero-title">INFORM.<br>INFLUENCE.<br>SELL.</h1>

<!-- challenge -->
<div class="abs maze-photo" role="img" aria-label="Businessman with a briefcase standing before a large white maze"></div>
<h2 class="abs section-title challenge-title">The Big Challenge</h2>
<p class="abs copy challenge-copy">In today’s competitive business environment, effective communication is more essential than ever before. It is the foundation upon which companies are built, careers are propelled, and knowledge is imparted. Effective communication is critical – without it, misunderstandings arise, errors occur, and business goals are frustrated. In short, effective communication is the key driver of long-term business and professional success.</p>

<!-- how we help -->
<div class="abs help-band"></div>
<div class="abs meeting-photo" role="img" aria-label="Presenter pointing at a chart on a wall screen in front of colleagues in a lounge"></div>
<h2 class="abs section-title help-title">How We Help</h2>
<p class="abs copy help-copy">At Marble Finch, we help individuals and organizations “get what they want” through clear and persuasive communication. Our consulting, coaching, and training services help clients achieve targeted business objectives, with an emphasis on informing, influencing, and selling.</p>

<!-- expertise -->
<div class="abs expertise"></div>
<h2 class="abs section-title expertise-title">Expertise</h2>

<div class="abs card" style="left:79px;top:1652px">
  <svg viewBox="0 0 76 76"><rect x="26" y="8" width="42" height="30" rx="2"/><line x1="33" y1="18" x2="60" y2="18"/><line x1="33" y1="25" x2="55" y2="25"/><line x1="47" y1="38" x2="47" y2="60"/><circle cx="16" cy="22" r="6"/><path d="M8 60V38c0-5 4-8 8-8h12l6-6"/></svg>
  <span class="label">Sales Training</span>
</div>
<div class="abs card" style="left:293px;top:1652px">
  <svg viewBox="0 0 76 76"><path d="M12 44l30-24 6 26-36-2z"/><path d="M18 45l4 16h8l-3-16"/><line x1="52" y1="14" x2="58" y2="6"/><line x1="56" y1="26" x2="66" y2="24"/><line x1="50" y1="36" x2="60" y2="40"/></svg>
  <span class="label">Marketing<br>Collateral</span>
</div>
<div class="abs card" style="left:505px;top:1652px">
  <svg viewBox="0 0 76 76"><rect x="30" y="6" width="38" height="26"/><polyline points="36,26 44,18 52,22 62,12"/><circle cx="14" cy="14" r="5"/><circle cx="14" cy="46" r="5"/><circle cx="38" cy="46" r="5"/><circle cx="62" cy="46" r="5"/><path d="M4 66c0-7 4-11 10-11s10 4 10 11M28 66c0-7 4-11 10-11s10 4 10 11M52 66c0-7 4-11 10-11s10 4 10 11"/></svg>
  <span class="label">Presentation<br>Skills Training</span>
</div>
<div class="abs card" style="left:719px;top:1652px">
  <svg viewBox="0 0 76 76"><circle cx="38" cy="22" r="12"/><circle cx="38" cy="22" r="5"/><path d="M6 44l16-8 14 8 6-2M70 44l-16-8-10 4"/><path d="M24 46l10 10 8-6 10 8 14-14"/></svg>
  <span class="label">Business<br>Presentations<br>&amp; Decks</span>
</div>
<div class="abs card" style="left:931px;top:1652px">
  <svg viewBox="0 0 76 76"><rect x="12" y="6" width="30" height="18" rx="6"/><rect x="36" y="14" width="30" height="18" rx="6"/><circle cx="20" cy="46" r="6"/><circle cx="56" cy="46" r="6"/><path d="M8 68c0-8 5-12 12-12s12 4 12 12M44 68c0-8 5-12 12-12s12 4 12 12"/></svg>
  <span class="label">Stage Talks</span>
</div>

<div class="abs card" style="left:79px;top:1890px">
  <svg viewBox="0 0 76 76"><circle cx="38" cy="16" r="10"/><path d="M38 26v16M38 42c-6-8-14-10-20-8M38 42c6-8 14-10 20-8"/><path d="M6 58l16-6h14l-10 6M20 70l22-2 26-16"/></svg>
  <span class="label">Venture Capital<br>Presentations<br>&amp; Decks</span>
</div>
<div class="abs card" style="left:293px;top:1890px">
  <svg viewBox="0 0 76 76"><rect x="8" y="8" width="46" height="36"/><line x1="16" y1="18" x2="40" y2="18"/><line x1="16" y1="26" x2="34" y2="26"/><circle cx="58" cy="30" r="7"/><path d="M48 66V48c0-6 5-9 10-9s10 3 10 9v18"/></svg>
  <span class="label">Elevator Pitches</span>
</div>
<div class="abs card" style="left:505px;top:1890px">
  <svg viewBox="0 0 76 76"><rect x="22" y="4" width="30" height="66" rx="4"/><rect x="36" y="18" width="30" height="18" rx="3"/><rect x="8" y="40" width="30" height="16" rx="3"/><line x1="34" y1="64" x2="40" y2="64"/></svg>
  <span class="label">Convention<br>&amp; Trade Show<br>Messaging</span>
</div>
<div class="abs card" style="left:719px;top:1890px">
  <svg viewBox="0 0 76 76"><path d="M24 6h44v30H56v8l-8-8H24z"/><path d="M8 22h40v30H24l-10 8v-8H8z"/><line x1="16" y1="32" x2="40" y2="32"/><line x1="16" y1="40" x2="34" y2="40"/></svg>
  <span class="label">Keynote<br>Speeches</span>
</div>
<div class="abs card" style="left:931px;top:1890px">
  <svg viewBox="0 0 76 76"><rect x="6" y="16" width="64" height="44"/><polyline points="6,16 38,42 70,16"/></svg>
  <span class="label">Corporate<br>&amp; Website<br>Messaging</span>
</div>

<!-- clients -->
<h2 class="abs section-title clients-title">Our Clients</h2>
<div class="abs client" style="left:152px;top:2355px">Riverton Bar</div>
<div class="abs client" style="left:335px;top:2355px">Lindell Holdings</div>
<div class="abs client" style="left:518px;top:2355px">Corvane</div>
<div class="abs client" style="left:701px;top:2355px">Tallow Realty</div>
<div class="abs client" style="left:884px;top:2355px">Brenmar Build</div>
<div class="abs client" style="left:244px;top:2471px">Ostrand</div>
<div class="abs client" style="left:427px;top:2471px">Vantly</div>
<div class="abs client" style="left:610px;top:2471px">Pellham Brands</div>
<div class="abs client" style="left:793px;top:2471px">Aldridge &amp; Co.</div>
<div class="abs dot" style="left:556px"></div>
<div class="abs dot" style="left:575px"></div>
<div class="abs dot" style="left:594px"></div>
<div class="abs dot" style="left:613px"></div>
<div class="abs dot" style="left:632px"></div>

<!-- results -->
<div class="abs results-band"></div>
<div class="abs results-photo" role="img" aria-label="Person on a mountain peak at sunrise beneath large 2022 numerals above the clouds"></div>
<h2 class="abs section-title results-title">Results</h2>
<p class="abs copy results-copy">Whatever the message, and whatever the medium, we help clients establish a connection, make an impression, and drive audiences toward a predetermined course of action. This results in clear messaging, captivated audiences, and increased sales.</p>

<!-- contact -->
<h2 class="abs section-title connect-title">Let's Connect</h2>
<div class="abs field" style="left:321px;top:3282px;width:269px">First Name</div>
<div class="abs field" style="left:609px;top:3282px;width:270px">Last Name</div>
<div class="abs field" style="left:321px;top:3338px;width:269px">Email</div>
<div class="abs field" style="left:609px;top:3338px;width:270px">Phone</div>
<div class="abs field" style="left:321px;top:3393px;width:558px">Address</div>
<div class="abs field" style="left:321px;top:3448px;width:558px;height:138px">Message</div>
<div class="abs submit">SUBMIT</div>

<!-- footer -->
<div class="abs footer"></div>
<div class="abs logo footer-logo">MARBLE &amp;<br>FINCH</div>
<div class="abs footer-rule"></div>
<nav class="footer-nav nav abs" style="top:0;left:0">
  <a style="left:584px;top:3717px" href="#">HOME</a>
  <a style="left:660px;top:3717px" href="#">FINCHCAMP</a>
  <a style="left:777px;top:3717px" href="#">TESTIMONIALS</a>
  <a style="left:913px;top:3717px" href="#">TEAM</a>
  <a style="left:986px;top:3717px" href="#">CONTACT</a>
</nav>
<p class="abs copyright">2022 Marble Finch Communications</p>

</body>
</html>
```